Harborline Security and Surveillance Business Card

Business Card Design - Company Name:Freedom Security and SurveillanceWe are a Security Systems Integrator Specializing in Security Systems/ Video Surveillance and Access Control. Our areas of expertise are:Security SystemsVideo SurveillanceAccess ControlFire Alarm SystemsNetwork CablingCellular BoostersMy input is the Front of the Card is: logo, name of Business, My Name, Phone Number, and email.Rear of Card is the 6 areas of expertise, I just dont want the front to be very busy.
Name: Tom Werner
Title: President
Email: tom@harborlinesecsys.example
website: harborlinesecsys.example

```html
<!DOCTYPE html>
<html lang="en">
<head>
<meta charset="utf-8">
<title>Harborline Security and Surveillance Business Card</title>
<link rel="stylesheet" href="https://fonts.googleapis.com/css2?family=Exo+2:wght@300;400;600&display=swap">
<style>
  :root {
    --brand-blue: #2a5caa;
    --ink: #1f1f1f;
    --muted: #6b6b6b;
    --rule: #b9b9b9;
    --paper: #ffffff;
    --backdrop: #3a3a3a;
    --silver-light: #e4e4e4;
    --silver-dark: #8a8a8a;
  }
  * { box-sizing: border-box; margin: 0; padding: 0; }
  html, body { width: 1200px; height: 987px; overflow: hidden; }
  body {
    background: var(--backdrop);
    font-family: "Exo 2", sans-serif;
    position: relative;
  }
  .card {
    position: absolute;
    width: 560px;
    height: 320px;
    background: var(--paper);
    overflow: hidden;
    box-shadow: 0 10px 30px rgba(0,0,0,0.45);
  }
  /* Back of card: services */
  .card-back { left: 70px; top: 90px; display: flex; }
  .services-panel {
    width: 255px;
    height: 100%;
    background: var(--brand-blue);
    color: var(--paper);
    padding: 58px 0 0 30px;
  }
  .services-title {
    font-weight: 400;
    font-size: 15px;
    letter-spacing: 1px;
    text-transform: uppercase;
    margin-bottom: 14px;
  }
  .services-list { list-style: none; }
  .services-list li {
    font-weight: 300;
    font-size: 14px;
    line-height: 27px;
    padding-left: 16px;
    position: relative;
  }
  .services-list li::before {
    content: "";
    position: absolute;
    left: 2px; top: 12px;
    width: 5px; height: 5px;
    border-radius: 50%;
    background: var(--paper);
  }
  .brand-panel {
    flex: 1;
    display: flex;
    align-items: center;
    justify-content: center;
    padding-bottom: 50px;
  }
  .wordmark {
    display: flex;
    align-items: center;
    gap: 10px;
    color: var(--brand-blue);
    font-weight: 600;
    text-transform: uppercase;
    letter-spacing: 1.5px;
    line-height: 1.15;
  }
  .wordmark-dot {
    width: 34px; height: 34px;
    border-radius: 50%;
    background: var(--brand-blue);
    flex: none;
  }
  .brand-panel .wordmark { font-size: 16px; }
  /* Front of card: contact */
  .card-front { left: 570px; top: 560px; }
  .card-front .wordmark {
    position: absolute;
    right: 34px; top: 34px;
    font-size: 15px;
  }
  .divider {
    position: absolute;
    left: 60px; right: 30px; top: 165px;
    height: 1px;
    background: var(--rule);
  }
  .contact { position: absolute; left: 60px; top: 178px; }
  .contact-name {
    color: var(--brand-blue);
    font-weight: 600;
    font-size: 16px;
    letter-spacing: 0.5px;
    text-transform: uppercase;
  }
  .contact-title {
    font-weight: 300;
    font-size: 11px;
    color: var(--muted);
    margin-bottom: 16px;
  }
  .contact-line {
    display: flex;
    align-items: center;
    gap: 10px;
    font-size: 13px;
    color: var(--ink);
    margin-bottom: 8px;
  }
  .contact-line svg { width: 17px; height: 17px; flex: none; }
  .footer-band { position: absolute; left: 0; bottom: 0; width: 560px; height: 70px; }
  .website {
    position: absolute;
    left: 120px; bottom: 14px;
    color: var(--paper);
    font-size: 13px;
    letter-spacing: 0.3px;
  }
</style>
</head>
<body>
  <section class="card card-back">
    <div class="services-panel">
      <h2 class="services-title">Our Services</h2>
      <ul class="services-list">
        <li>Security Systems</li>
        <li>Video Surveillance</li>
        <li>Access Control</li>
        <li>Fire Alarm Systems</li>
        <li>Network Cabling</li>
        <li>Cellular Boosters</li>
      </ul>
    </div>
    <div class="brand-panel">
      <div class="wordmark"><span class="wordmark-dot"></span><span>Harborline Security<br>and Surveillance</span></div>
    </div>
  </section>

  <section class="card card-front">
    <div class="wordmark"><span class="wordmark-dot"></span><span>Harborline Security<br>and Surveillance</span></div>
    <div class="divider"></div>
    <div class="contact">
      <p class="contact-name">Tom Werner</p>
      <p class="contact-title">President</p>
      <p class="contact-line">
        <svg viewBox="0 0 18 18" aria-hidden="true"><circle cx="9" cy="9" r="8" fill="none" stroke="#2a5caa" stroke-width="1"/><rect x="4.5" y="6" width="9" height="6.5" fill="none" stroke="#2a5caa" stroke-width="1"/><path d="M4.5 6 L9 9.5 L13.5 6" fill="none" stroke="#2a5caa" stroke-width="1"/></svg>
        tom@harborlinesecsys.example
      </p>
      <p class="contact-line">
        <svg viewBox="0 0 18 18" aria-hidden="true"><circle cx="9" cy="9" r="8" fill="none" stroke="#2a5caa" stroke-width="1"/><path d="M6 5 L7.6 5 L8.3 7.2 L7.3 8 Q8.3 10 10 10.8 L10.8 9.8 L13 10.5 L13 12 Q12.5 13 11 13 Q6 12 5 7 Q5 5.5 6 5 Z" fill="none" stroke="#2a5caa" stroke-width="1"/></svg>
        +610 555 0142 000
      </p>
    </div>
    <svg class="footer-band" viewBox="0 0 560 70" aria-hidden="true">
      <defs>
        <linearGradient id="silver-swoosh" x1="0" y1="0" x2="1" y2="0">
          <stop offset="0" stop-color="#8a8a8a"/>
          <stop offset="0.6" stop-color="#e4e4e4"/>
          <stop offset="1" stop-color="#c8c8c8"/>
        </linearGradient>
      </defs>
      <path d="M300 30 C312 30 316 18 330 16 L560 16 L560 26 L330 26 C318 26 312 36 300 36 Z" fill="url(#silver-swoosh)"/>
      <path d="M0 42 L250 42 C275 42 282 24 305 24 L560 24 L560 70 L0 70 Z" fill="#2a5caa"/>
    </svg>
    <p class="website">www.harborlinesecsys.example</p>
  </section>
</body>
</html>
```